Invitation Flyer for the event with 3 workshops

A flyer with inputs noted in attached wordfile. It's for women only so the layout is inspire business women.

Target Market(s)

Working women, with or without family

Industry/Entity Type

Business

Font styles to use
Sans Serif

Colors

Designer to choose colors to be used in the design.

Requirements
Must have
• All information that is on the flyer.
Nice to have
• It should look professional, but still inviting and inspiring.

```html
<!DOCTYPE html>
<html lang="en">
<head>
<meta charset="utf-8">
<title>Women's Business Network – Workshop Day Invitation</title>
<link href="https://fonts.googleapis.com/css2?family=Roboto+Condensed:ital,wght@0,400;0,700;0,900;1,700;1,900&family=Open+Sans:wght@400;700&family=Dancing+Script:wght@700&display=swap" rel="stylesheet">
<style>
:root{
  --yellow:#f7d117;
  --black:#111111;
  --white:#ffffff;
  --grey:#8a8a8a;
  --grey-light:#d9d9d9;
  --red:#d4281e;
  --page-bg:#ffffff;
}
*{box-sizing:border-box;margin:0;padding:0}
html,body{width:813px;height:1200px;overflow:hidden;background:var(--page-bg)}
body{position:relative;font-family:"Open Sans",Arial,sans-serif;color:var(--black)}
.panel{position:absolute;overflow:hidden}
.side-label{position:absolute;font-family:"Roboto Condensed",Arial,sans-serif;font-weight:900;font-size:30px;letter-spacing:1px}

/* brand */
.brand{display:flex;align-items:center;gap:7px}
.brand-mark{width:26px;height:26px;border-radius:50%;background:var(--yellow);flex:none}
.brand-name{font-family:"Roboto Condensed",Arial,sans-serif;font-weight:700;font-size:19px;line-height:1}
.brand-sub{font-family:"Roboto Condensed",Arial,sans-serif;font-weight:700;font-size:12px;line-height:1.2}

/* date badge */
.date-badge{position:absolute;z-index:2;background:var(--yellow);text-align:center;font-family:"Roboto Condensed",Arial,sans-serif}
.date-badge .day{font-weight:900;font-style:italic;font-size:17px;padding:3px 6px;color:var(--black)}
.date-badge .time{background:var(--black);color:var(--white);font-weight:900;font-size:16px;line-height:1.2;padding:3px 6px}
.date-badge .venue{background:var(--black);color:var(--white);font-size:8px;font-weight:700;padding:2px 4px 4px;line-height:1.2}
sup{font-size:.6em}

/* BACK */
.back{left:14px;top:8px;width:392px;height:380px;background:var(--white);border:3px solid var(--black)}
.back .brand{position:absolute;left:10px;top:10px}
.back .date-badge{right:10px;top:8px;width:120px}
.back .event-title{position:absolute;left:0;top:66px;width:230px;background:var(--black);color:var(--white);font-family:"Roboto Condensed",Arial,sans-serif;font-weight:900;font-size:21px;padding:6px 10px}
.back .venue-line{position:absolute;left:10px;top:104px;font-family:"Roboto Condensed",Arial,sans-serif;font-size:10px;line-height:1.3}
.back .venue-line b{font-size:11px}
.back .photo-seated{position:absolute;left:236px;top:66px;width:146px;height:92px;background:linear-gradient(160deg,#f3f3f3,#c9c9c9 60%,#e9e0b0)}
.back .choose{position:absolute;left:10px;top:132px;font-family:"Dancing Script",cursive;font-size:19px;color:var(--red)}
.workshop{position:absolute;width:180px}
.workshop .head{display:flex;align-items:center;gap:6px}
.workshop .tick{width:16px;height:16px;border:2px solid var(--black);background:var(--white);flex:none}
.workshop .name{flex:1;background:var(--black);color:var(--yellow);font-family:"Roboto Condensed",Arial,sans-serif;font-weight:700;font-size:11px;padding:2px 5px}
.workshop .desc{margin-left:22px;background:var(--yellow);font-size:7.5px;line-height:1.25;padding:3px 5px}
.ws1{left:8px;top:162px}.ws2{left:200px;top:162px}.ws3{left:200px;top:216px}
.deadline{position:absolute;left:8px;top:214px;width:180px;height:46px;background:var(--yellow);padding:3px 8px}
.deadline .lbl{font-family:"Roboto Condensed",Arial,sans-serif;font-weight:900;font-size:16px}
.deadline .date{font-family:"Dancing Script",cursive;font-size:19px;color:var(--red);line-height:1}
.form{position:absolute;left:8px;top:270px;width:372px}
.form .row{display:flex;font-family:"Roboto Condensed",Arial,sans-serif;font-size:9px;font-weight:700;border-bottom:1px solid var(--grey);height:17px;align-items:flex-end;padding-bottom:1px}
.form .row span{flex:1}
.send{position:absolute;left:8px;bottom:8px;width:372px;font-size:8px;display:flex;gap:10px;line-height:1.3}
.send b{font-weight:700}

/* FRONT */
.front{left:412px;top:8px;width:392px;height:380px;background:var(--black);border:4px solid var(--yellow)}
.front .brand{position:absolute;left:12px;top:14px;color:var(--white)}
.front .date-badge{right:8px;top:6px;width:112px}
.front .title-band{position:absolute;left:0;top:70px;width:100%;background:var(--yellow);padding:6px 10px;font-family:"Roboto Condensed",Arial,sans-serif}
.front .title-band h1{font-size:19px;font-weight:900;line-height:1.1}
.front .title-band p{font-size:14px;font-weight:700;margin-top:2px}
.front .photo-group{position:absolute;left:0;top:122px;width:100%;height:160px;background:linear-gradient(180deg,#e9d663,#cfc7b6 45%,#7d7368)}
.front .url{position:absolute;left:0;top:282px;width:100%;background:var(--white);text-align:right;padding:3px 12px;font-family:"Roboto Condensed",Arial,sans-serif;font-weight:700;font-size:11px;border-bottom:1px solid var(--grey-light)}
.front .partner{position:absolute;left:0;top:300px;width:100%;height:72px;background:var(--white);display:flex;align-items:center;justify-content:center;gap:8px}
.front .partner .mark{width:30px;height:30px;background:var(--yellow)}
.front .partner .name{font-family:"Roboto Condensed",Arial,sans-serif;font-weight:700;font-size:24px;color:var(--black)}

/* INSIDE */
.inside{top:430px;width:392px;height:732px;background:var(--white)}
.inside-left{left:10px}.inside-right{left:411px}
.speaker{position:absolute;left:0;width:392px;height:360px;border:5px solid var(--yellow);background:var(--white)}
.speaker .strip{height:38px;background:var(--black);color:var(--yellow);font-family:"Roboto Condensed",Arial,sans-serif;font-style:italic;font-weight:900;font-size:20px;text-align:right;padding:6px 14px}
.speaker .band{position:absolute;left:0;top:58px;width:100%;height:56px;background:linear-gradient(90deg,#4a4a4a,#9b9b9b 60%,#d6d6d6);padding:6px 0 0 112px;color:var(--white);font-family:"Roboto Condensed",Arial,sans-serif}
.speaker .band .nm{font-size:24px;font-weight:900;line-height:1}
.speaker .band .tt{font-size:13px;font-weight:700}
.speaker .portrait{position:absolute;left:12px;top:44px;width:90px;height:90px;border-radius:50%;border:3px solid var(--white);background:linear-gradient(160deg,#e6d3bf,#8a6f58)}
.speaker .topic{position:absolute;left:12px;top:140px;font-family:"Roboto Condensed",Arial,sans-serif;font-weight:900;font-size:22px}
.speaker .lead{position:absolute;left:0;top:170px;width:100%;background:var(--yellow);font-size:9.5px;font-weight:700;line-height:1.3;padding:5px 12px}
.speaker .body{position:absolute;left:12px;top:222px;right:12px;font-size:8.5px;color:#555;line-height:1.35}
.speaker .url{position:absolute;left:0;bottom:0;width:100%;background:var(--black);color:var(--white);text-align:center;font-family:"Roboto Condensed",Arial,sans-serif;font-weight:700;font-size:13px;padding:6px}
.s1{top:0}.s3{top:372px}.s2{top:0}
.join{position:absolute;left:0;top:372px;width:392px;height:360px;border:5px solid var(--yellow);background:var(--black)}
.join .photo-trio{position:absolute;left:0;top:0;width:100%;height:240px;background:linear-gradient(180deg,#c9c2bb,#8f7e70 60%,#3b3430)}
.join .cta{position:absolute;left:60px;top:262px;width:262px;background:var(--yellow);text-align:center;font-family:"Roboto Condensed",Arial,sans-serif;font-weight:900;font-size:24px;line-height:1.1;padding:10px}
.fold-dot{position:absolute;left:394px;top:784px;width:24px;height:24px;border-radius:50%;background:var(--white);border:2px solid var(--grey)}
</style>
</head>
<body>

<section class="panel back">
  <div class="brand">
    <div class="brand-mark"></div>
    <div><div class="brand-name">WBN ALPINA</div><div class="brand-sub">Women's Business Network</div></div>
  </div>
  <div class="date-badge">
    <div class="day">JULY 15<sup>th</sup></div>
    <div class="time">10AM–6PM</div>
  </div>
  <div class="event-title">TITLE OF THE EVENT</div>
  <div class="venue-line"><b>EVENT CENTRE</b><br>event centre address</div>
  <div class="photo-seated" role="img" aria-label="Photo of a smiling businesswoman seated in a chair"></div>
  <div class="choose">Please choose 2 workshops</div>

  <div class="workshop ws1">
    <div class="head"><div class="tick"></div><div class="name">WORKSHOP 1 TITLE</div></div>
    <div class="desc">Short description of the content: with box ahead of the titles so that persons can choose 2 workshops</div>
  </div>
  <div class="workshop ws2">
    <div class="head"><div class="tick"></div><div class="name">WORKSHOP 2 TITLE</div></div>
    <div class="desc">Short description of the content: with box ahead of the titles so that persons can choose 2 workshops</div>
  </div>
  <div class="workshop ws3">
    <div class="head"><div class="tick"></div><div class="name">WORKSHOP 3 TITLE</div></div>
    <div class="desc">Short description of the content: with box ahead of the titles so that persons can choose 2 workshops</div>
  </div>
  <div class="deadline">
    <div class="lbl">Application Deadline</div>
    <div class="date">June 15th 2018</div>
  </div>

  <div class="form">
    <div class="row"><span>NAME</span></div>
    <div class="row"><span>ADDRESS</span></div>
    <div class="row"><span>COMPANY</span><span>TEL</span></div>
  </div>
  <div class="send">
    <span>Please send the application to:</span>
    <span><b>address of WBN, address of WBN</b><br><b>address of WBN, address of WBN</b></span>
  </div>
</section>

<section class="panel front">
  <div class="brand">
    <div class="brand-mark"></div>
    <div><div class="brand-name">WBN ALPINA</div><div class="brand-sub">Women's Business Network</div></div>
  </div>
  <div class="date-badge">
    <div class="day">JULY 15<sup>th</sup></div>
    <div class="time">10AM–6PM</div>
    <div class="venue"><b>EVENT CENTRE</b><br>event centre address</div>
  </div>
  <div class="title-band">
    <h1>TITLE OF THE EVENT WITH THE 3 TOPICS</h1>
    <p>TOPIC 1 | TOPIC 2 | TOPIC 3</p>
  </div>
  <div class="photo-group" role="img" aria-label="Photo of three confident businesswomen standing together"></div>
  <div class="url">WWW.SHEFORWARD.CH</div>
  <div class="partner"><div class="mark"></div><div class="name">SHE FORWARD</div></div>
</section>

<div class="side-label" style="left:14px;top:392px">BACK</div>
<div class="side-label" style="right:12px;top:392px">FRONT</div>

<section class="panel inside inside-left">
  <article class="speaker s1">
    <div class="strip">JULY 15<sup>th</sup> AT 10AM</div>
    <div class="band"><div class="nm">SPEAKER NAME</div><div class="tt">SPEAKER TITLE</div></div>
    <div class="portrait" role="img" aria-label="Portrait photo of speaker one"></div>
    <div class="topic">TOPIC TITLE</div>
    <div class="lead">Short description of the content: with box ahead of the titles so that persons can choose 2 workshops. Short description of the content with box ahead of the titles.</div>
    <p class="body">Short description of the content with more details about the workshop, the speaker and what guests will take home from this session.</p>
    <div class="url">WWW.SPEAKERSTUDIO.NET</div>
  </article>
  <article class="speaker s3">
    <div class="strip">JULY 15<sup>th</sup> AT 10AM</div>
    <div class="band"><div class="nm">SPEAKER NAME</div><div class="tt">SPEAKER TITLE</div></div>
    <div class="portrait" role="img" aria-label="Portrait photo of speaker three"></div>
    <div class="topic">TOPIC TITLE</div>
    <div class="lead">Short description of the content: with box ahead of the titles so that persons can choose 2 workshops. Short description of the content with box ahead of the titles.</div>
    <p class="body">Short description of the content with more details about the workshop, the speaker and what guests will take home from this session.</p>
    <div class="url">WWW.SPEAKERSTUDIO.NET</div>
  </article>
</section>

<section class="panel inside inside-right">
  <article class="speaker s2">
    <div class="strip">JULY 15<sup>th</sup> AT 10AM</div>
    <div class="band"><div class="nm">SPEAKER NAME</div><div class="tt">SPEAKER TITLE</div></div>
    <div class="portrait" role="img" aria-label="Portrait photo of speaker two"></div>
    <div class="topic">TOPIC TITLE</div>
    <div class="lead">Short description of the content: with box ahead of the titles so that persons can choose 2 workshops. Short description of the content with box ahead of the titles.</div>
    <p class="body">Short description of the content with more details about the workshop, the speaker and what guests will take home from this session.</p>
    <div class="url">WWW.SPEAKERSTUDIO.NET</div>
  </article>
  <div class="join">
    <div class="photo-trio" role="img" aria-label="Photo of three smiling women side by side"></div>
    <div class="cta">JOIN US FOR AN<br>AWESOME DAY</div>
  </div>
</section>

<div class="fold-dot"></div>

<div class="side-label" style="left:14px;top:1162px">INSIDE</div>
<div class="side-label" style="right:12px;top:1162px">INSIDE</div>

</body>
</html>
```